Sports Supplements Company Needs Label Designs

Hello,

We are a sports supplements company named "Vantor Kinetics". We produce a line of sports supplements from pre-workouts products to fat burners and multivitamins. Our competitors include companies like Calloway Fuelworks and BrawnLabix. Like most companies in the sports supplements field, we need a standard label design for one product that can be later modified a little to be used for the other products. Initially we need a label design for our "BCAA (Branched-Chain Amino Acids)" product. We would like to add other supplements like glutamine and fat burners, so we need a standard design that can be tweaked a bit. The only difference would be the information and ingredients in the other products, which will be provided.

For the design we would like one that reflects a modern, brand-unique approach. It should communicate trust and quality. Competitors designs to be considered as reference would include QRN Athletix, BrawnLabix, and Vexamor. Photos of their products can be seen online in places like liftvaultz.example. We would also like to include a couple of small icons to indicate the respective product's main functions. Similar icons can be seen in TKL Nourish products, as an example. Main qualities of the BCAA is "strength", "recovery", "Muscle Growth". The product's name is BCAA Torvalis.

The package will be white, with an undecided lid color (probably black). Color combinations I have in mind are mixed combinations of any of the following colors: red, white, yellow (some light to darker shades), brown, black, green, and blue. But please this does not have to limit your imagination to the design and colors. These are just ideas from top of my head. Since the company's name is Vantor Kinetics, I do like the design to represent some sort of "mechanics": I'd like to have some design that includes watch wheels, and maybe a wrench. I also would like the name of the company to be on the label as well, under the logo.

Other project text details and measurements are provided in an attached word document, along with the logo of the company we like to use. We like the format to be Ai.

We'd like a designer to work with in future products, and build a relationship with. As said earlier, we need to hire a designer to work with and modify similar projects with a fixed amount (~$50) for each additional product.

Industry/Entity Type

It Company

Colors
f37122
f78f20
ffc214
fbed22
9bcb3c
ec1f27
0255a3
ffffff
000000

Requirements
Must have
• Some sort of "mechanics": I'd like to have some design that includes watch wheels, and maybe a wrench.
Nice to have
• Some sort of harmonious color mixes. Mixes of yellow or orange with white, or maybe red and black.
Should not have
• Plain label with no designs.
• A simple design.

```html
<!DOCTYPE html>
<html lang="en">
<head>
<meta charset="utf-8">
<title>BCAA Torvalis Label – Vantor Kinetics</title>
<link href="https://fonts.googleapis.com/css2?family=Russo+One&family=Montserrat:wght@500;700&family=Roboto+Mono:wght@700&display=swap" rel="stylesheet">
<style>
  :root {
    --canvas: #f4f5f6;
    --label: #ffffff;
    --ink: #0b0b0c;
    --blue: #1e8fe0;
    --blue-deep: #0255a3;
    --chrome-light: #e6e8ea;
    --chrome-dark: #6c7076;
    --motif: #eceef0;
    --white: #ffffff;
  }
  * { margin: 0; padding: 0; box-sizing: border-box; }
  html, body { width: 1200px; height: 900px; overflow: hidden; background: var(--canvas); }
  .label {
    position: absolute; left: 330px; top: 270px; width: 540px; height: 480px;
    background: var(--label); box-shadow: 0 2px 14px rgba(0,0,0,.08);
    overflow: hidden;
  }
  .chrome-stripe {
    position: absolute; left: 0; width: 100%; height: 12px;
    background: linear-gradient(90deg, var(--chrome-dark), var(--chrome-light) 20%, var(--chrome-dark) 45%, var(--chrome-light) 70%, var(--chrome-dark));
  }
  .chrome-stripe.top { top: 24px; border-bottom: 3px solid var(--blue); }
  .brand-plate {
    position: absolute; top: 8px; left: 50%; transform: translateX(-50%);
    width: 262px; height: 52px; background: var(--ink);
    border-left: 3px solid var(--blue); border-right: 3px solid var(--blue);
    color: var(--white); font-family: "Montserrat", sans-serif; font-weight: 700;
    font-size: 15px; letter-spacing: 1px; display: flex; align-items: center; justify-content: center;
  }
  .motif {
    position: absolute; left: 60px; top: 80px; width: 420px; height: 330px;
    background: radial-gradient(circle at 50% 55%, var(--motif) 0 40%, rgba(236,238,240,.5) 60%, transparent 72%);
  }
  .product-name {
    position: absolute; left: 0; width: 100%; text-align: center;
    font-family: "Russo One", sans-serif; color: var(--ink);
    -webkit-text-stroke: 2px var(--blue);
    text-shadow: 0 0 1px var(--blue), 3px 3px 0 rgba(30,143,224,.35);
    line-height: 1;
  }
  .product-name.line-one { top: 146px; font-size: 82px; letter-spacing: 2px; }
  .product-name.line-two { top: 220px; font-size: 70px; letter-spacing: 1px; }
  .strength-bar {
    position: absolute; top: 283px; left: 50%; transform: translateX(-50%) skewX(-12deg);
    width: 380px; height: 27px; background: var(--ink); border-bottom: 2px solid var(--blue);
    display: flex; align-items: center; justify-content: center;
  }
  .strength-bar span {
    transform: skewX(12deg); color: var(--white);
    font-family: "Roboto Mono", monospace; font-weight: 700; font-size: 17px; letter-spacing: 7px;
  }
  .benefit-icons { position: absolute; top: 318px; left: 0; width: 100%; height: 64px; }
  .benefit-bar {
    position: absolute; top: 378px; left: 120px; width: 300px; height: 13px;
    background: linear-gradient(90deg, var(--blue-deep), var(--blue), var(--blue-deep));
    display: flex; justify-content: space-around; align-items: center;
    font-family: "Montserrat", sans-serif; font-weight: 700; font-size: 8px; color: var(--white);
  }
  .checklist {
    position: absolute; top: 398px; left: 0; width: 100%;
    display: flex; justify-content: center; gap: 12px;
    font-family: "Roboto Mono", monospace; font-weight: 700; font-size: 10px; color: var(--ink);
  }
  .checklist li { list-style: none; display: flex; align-items: center; gap: 3px; }
  .tick { width: 10px; height: 10px; }
  .blue-rule { position: absolute; left: 0; top: 452px; width: 100%; height: 4px; background: var(--blue); }
  .count-tab {
    position: absolute; top: 436px; left: 50%; transform: translateX(-50%);
    width: 170px; height: 44px; background: var(--ink); border-radius: 14px 14px 0 0;
    text-align: center; padding-top: 7px; font-family: "Roboto Mono", monospace; font-weight: 700;
  }
  .count-tab .count { display: block; color: var(--white); font-size: 12px; letter-spacing: 1px; }
  .count-tab .kind { display: block; color: var(--blue); font-size: 10px; letter-spacing: 1px; }
</style>
</head>
<body>
  <main class="label">
    <div class="motif" role="img" aria-label="Faint large gear and wrench motif behind the product name"></div>
    <div class="chrome-stripe top"></div>
    <div class="brand-plate">VANTOR <span style="font-weight:500">&nbsp;KINETICS</span></div>

    <h1 class="product-name line-one">BCAA</h1>
    <h1 class="product-name line-two">TORVALIS</h1>

    <div class="strength-bar"><span>ULTRA STRENGTH</span></div>

    <svg class="benefit-icons" viewBox="0 0 540 64" width="540" height="64">
      <defs>
        <g id="gear-badge">
          <g fill="#0b0b0c">
            <rect x="-5" y="-31" width="10" height="62" rx="2"/>
            <rect x="-5" y="-31" width="10" height="62" rx="2" transform="rotate(45)"/>
            <rect x="-5" y="-31" width="10" height="62" rx="2" transform="rotate(90)"/>
            <rect x="-5" y="-31" width="10" height="62" rx="2" transform="rotate(135)"/>
            <circle r="26"/>
          </g>
          <circle r="21" fill="none" stroke="#ffffff" stroke-width="1.5"/>
        </g>
      </defs>
      <g transform="translate(170,31)">
        <use href="#gear-badge"/>
        <circle r="12" fill="#ffffff" role="img" aria-label="Flexed arm icon for muscle building"/>
      </g>
      <g transform="translate(270,31)">
        <use href="#gear-badge"/>
        <circle cy="3" r="12" fill="none" stroke="#ffffff" stroke-width="3"/>
        <rect x="-3" y="-15" width="6" height="5" fill="#ffffff"/>
        <path d="M0 3 V-4 M0 3 L5 6" stroke="#ffffff" stroke-width="2.5" stroke-linecap="round"/>
      </g>
      <g transform="translate(370,31)">
        <use href="#gear-badge"/>
        <rect x="-8" y="-8" width="16" height="22" rx="3" fill="#ffffff"/>
        <rect x="-5" y="-14" width="10" height="5" rx="1" fill="#ffffff"/>
        <rect x="-8" y="0" width="16" height="3" fill="#0b0b0c"/>
      </g>
    </svg>

    <div class="benefit-bar">
      <span>MUSCLE BUILDING</span><span>RECOVERY</span><span>EASY MIX</span>
    </div>

    <ul class="checklist">
      <li><svg class="tick" viewBox="0 0 10 10"><rect width="10" height="10" fill="#0255a3"/><path d="M2 5 L4 7.5 L8 2.5" stroke="#fff" stroke-width="1.6" fill="none"/></svg>STIMULATES PROTEIN SYNTHESIS</li>
      <li><svg class="tick" viewBox="0 0 10 10"><rect width="10" height="10" fill="#0255a3"/><path d="M2 5 L4 7.5 L8 2.5" stroke="#fff" stroke-width="1.6" fill="none"/></svg>REDUCES MUSCLE BREAKDOWN</li>
      <li><svg class="tick" viewBox="0 0 10 10"><rect width="10" height="10" fill="#0255a3"/><path d="M2 5 L4 7.5 L8 2.5" stroke="#fff" stroke-width="1.6" fill="none"/></svg>SUPPORTS MUSCLE RECOVERY</li>
    </ul>

    <div class="blue-rule"></div>
    <div class="count-tab">
      <span class="count">120 TABLETS</span>
      <span class="kind">DIETARY SUPPLEMENT</span>
    </div>
  </main>
</body>
</html>
```